Creative Businesss Card desgin!

Create a business card for our business Glint window cleaning!
We are open to creative ideas as long as it maintains a professional image.

Target Market(s)

Small Commercial window cleaning clients including car dealerships, strata manager, cafe

Industry/Entity Type

Window Cleaning

Contact Information for Business Card

Darren Pilkey
General Manager
Glint Window Cleaning

darren@glintservices.com.au
pane-tidy-corner.com.au
Ph: 1800 GO GLINT
Mob: 0438 572 619

Colors
fbed22
0392cd

Requirements
Should not have
• Stock window cleaning/ squeegee graphics

```html
<!DOCTYPE html>
<html lang="en">
<head>
<meta charset="utf-8">
<title>Glint Window Cleaning – Business Card</title>
<link rel="stylesheet" href="https://fonts.googleapis.com/css2?family=Lato:wght@400;700;900&display=swap">
<style>
  :root {
    --page: #e6e8eb;
    --card-blue: #03507f;
    --pattern-blue: #17608f;
    --pattern-blue-soft: #0c5885;
    --glint-yellow: #f4ec1f;
    --text-white: #ffffff;
    --divider: rgba(255, 255, 255, 0.85);
  }
  * { margin: 0; padding: 0; box-sizing: border-box; }
  html, body {
    width: 1200px;
    height: 960px;
    overflow: hidden;
    background: var(--page);
    font-family: "Lato", sans-serif;
  }
  .canvas {
    position: relative;
    width: 1200px;
    height: 960px;
  }
  .card {
    position: absolute;
    left: 280px;
    width: 655px;
    height: 373px;
    border-radius: 16px;
    background: var(--card-blue);
    overflow: hidden;
    box-shadow: 0 4px 12px rgba(0, 0, 0, 0.18);
  }
  .card-front { top: 80px; }
  .card-back  { top: 506px; }

  /* Front */
  .brand-name {
    position: absolute;
    left: 82px;
    top: 150px;
    width: 218px;
    color: var(--glint-yellow);
    font-weight: 900;
    text-align: center;
    line-height: 1;
  }
  .brand-name .brand-main {
    display: block;
    font-size: 62px;
    letter-spacing: 3px;
  }
  .brand-name .brand-sub {
    display: block;
    margin-top: 6px;
    font-size: 19px;
    letter-spacing: 0.2px;
  }
  .divider {
    position: absolute;
    left: 329px;
    top: 106px;
    width: 1.5px;
    height: 161px;
    background: var(--divider);
  }
  .person {
    position: absolute;
    left: 361px;
    top: 105px;
  }
  .person-name {
    color: var(--glint-yellow);
    font-weight: 700;
    font-size: 26px;
    line-height: 1.2;
  }
  .person-title {
    color: var(--text-white);
    font-size: 16.5px;
    line-height: 1.2;
  }
  .contact-list {
    position: absolute;
    left: 366px;
    top: 180px;
    list-style: none;
  }
  .contact-item {
    display: flex;
    align-items: center;
    height: 22.3px;
    color: var(--text-white);
    font-size: 15.5px;
  }
  .contact-icon {
    width: 14px;
    height: 14px;
    margin-right: 9px;
    flex: none;
    fill: var(--glint-yellow);
  }

  /* Back */
  .back-pattern {
    position: absolute;
    inset: 0;
    background: linear-gradient(180deg, var(--pattern-blue) 0%, var(--pattern-blue-soft) 100%);
  }
  .back-mark {
    position: absolute;
    left: 92px;
    top: 208px;
    display: flex;
    align-items: center;
    gap: 10px;
    color: var(--glint-yellow);
    font-weight: 900;
    font-size: 40px;
    letter-spacing: 2px;
    line-height: 1;
  }
  .back-mark-dot {
    width: 14px;
    height: 14px;
    border-radius: 50%;
    background: var(--glint-yellow);
  }
</style>
</head>
<body>
<main class="canvas">

  <section class="card card-front" aria-label="Business card front">
    <div class="brand-name">
      <span class="brand-main">GLINT</span>
      <span class="brand-sub">WINDOW CLEANING</span>
    </div>

    <div class="divider"></div>

    <div class="person">
      <p class="person-name">Darren Pilkey</p>
      <p class="person-title">General Manager</p>
    </div>

    <ul class="contact-list">
      <li class="contact-item">
        <svg class="contact-icon" viewBox="0 0 16 16" aria-hidden="true">
          <path d="M4 1.5c.6-.4 1.3-.2 1.6.4l1.1 2.1c.3.6.1 1.2-.4 1.6l-.9.6c.2 1.5 1.3 3.6 2.6 4.8l1-.5c.6-.3 1.2-.1 1.6.4l1.3 2c.4.6.2 1.3-.4 1.6l-1 .6C7.5 15.6 1.8 8.6 2.9 2.3z"/>
        </svg>
        1800 GO GLINT
      </li>
      <li class="contact-item">
        <svg class="contact-icon" viewBox="0 0 16 16" aria-hidden="true">
          <path d="M4.5 1h7c.6 0 1 .4 1 1v12c0 .6-.4 1-1 1h-7c-.6 0-1-.4-1-1V2c0-.6.4-1 1-1zm.6 2v9.3h5.8V3zM8 13.2a.7.7 0 1 0 0 1.4.7.7 0 0 0 0-1.4z"/>
        </svg>
        0438 572 619
      </li>
      <li class="contact-item">
        <svg class="contact-icon" viewBox="0 0 16 16" aria-hidden="true">
          <path d="M1 3.5h14v9H1zm1.6 1.2L8 8.7l5.4-4zM2.2 11.3h11.6L9.9 7.9 8 9.3 6.1 7.9z"/>
        </svg>
        darren@glintservices.com.au
      </li>
      <li class="contact-item">
        <svg class="contact-icon" viewBox="0 0 16 16" aria-hidden="true">
          <path d="M8 1a7 7 0 1 0 0 14A7 7 0 0 0 8 1zm-.6 1.3v2.5H5.3c.5-1.3 1.2-2.2 2.1-2.5zm1.2 0c.9.3 1.6 1.2 2.1 2.5H8.6zM4.1 4.8H2.9a5.8 5.8 0 0 1 2.3-2c-.4.6-.8 1.3-1.1 2zm7.8 0c-.3-.7-.7-1.4-1.1-2a5.8 5.8 0 0 1 2.3 2zM2.3 6h1.5c-.1.6-.1 1.3-.1 2s0 1.4.1 2H2.3a5.8 5.8 0 0 1 0-4zm2.7 0h2.4v4H5c-.1-.6-.1-1.3-.1-2s0-1.4.1-2zm3.6 0H11c.1.6.1 1.3.1 2s0 1.4-.1 2H8.6zm3.6 0h1.5a5.8 5.8 0 0 1 0 4h-1.5c.1-.6.1-1.3.1-2s0-1.4-.1-2zM2.9 11.2h1.2c.3.7.7 1.4 1.1 2a5.8 5.8 0 0 1-2.3-2zm2.4 0h2.1v2.5c-.9-.3-1.6-1.2-2.1-2.5zm3.3 0h2.1c-.5 1.3-1.2 2.2-2.1 2.5zm3.3 0h1.2a5.8 5.8 0 0 1-2.3 2c.4-.6.8-1.3 1.1-2z"/>
        </svg>
        pane-tidy-corner.com.au
      </li>
    </ul>
  </section>

  <section class="card card-back" aria-label="Business card back">
    <div class="back-pattern" role="img" aria-label="Repeating pattern of faint brand symbols in lighter blue covering the card back"></div>
    <div class="back-mark">
      <span class="back-mark-dot" aria-hidden="true"></span>
      <span class="back-mark-name">GLINT</span>
    </div>
  </section>

</main>
</body>
</html>
```